Mobile (Android/iPhone) game studio needs stationary design and a business card

We are Brisk Pebble Software and we need a fun and creative stationary design. Our company builds Android and iPhone games and children's software. The stationary designs should reflect an entertainment, fun and creativity. The pieces of stationary we need are:
1. A4 and Letter Word template (company letterhead)
2. A4 and Letter PPT template
3. Business card
4. Envelopes of various standard sizes
Each of the designs should somehow utilize our company logo.
The business card should have the following:
1. Incorporates our company logo (see attached)
2. Has a front and back with the same design (front is English, back is Traditional Chinese)
3. Delivered in an editable template so we can easily add new business cards using the same template when we hire more employees
4. Field for full name
5. Field for employee's title
6. Field for employee's email address
7. Field for company phone number - +886-2-25118340
8. Field for mobile phone number
9. Field for company fax number - +886-2-25118472
10. Company website address: www.briskpebble-example.com
11. Company address (on English side): 2F-7, NO. 26, Lane 91, Fulin Road, Nei Hu District, Taipei Taiwan
12. Company address (on Traditional Chinese side): See Word document attachment for address in Chinese characters

```html
<!DOCTYPE html>
<html lang="en">
<head>
<meta charset="utf-8">
<title>Brisk Pebble Software — Stationery Set</title>
<link rel="stylesheet" href="https://fonts.googleapis.com/css2?family=Arimo:wght@400;700&family=Noto+Sans+TC:wght@400&display=swap">
<style>
  :root {
    --backdrop: #1c1d21;
    --paper: #eef0f3;
    --paper-white: #ffffff;
    --navy: #1b1d6b;
    --blue: #1658b0;
    --blue-deep: #0c3680;
    --sky: #2e97dd;
    --ink: #5b5f66;
    --rule-grey: #a9adb4;
  }
  html, body {
    margin: 0;
    padding: 0;
    width: 1200px;
    height: 900px;
    overflow: hidden;
    background: var(--backdrop);
    font-family: "Arimo", Arial, sans-serif;
  }
  .canvas { position: relative; width: 1200px; height: 900px; }
  .piece {
    position: absolute;
    overflow: hidden;
    box-shadow: 0 6px 18px rgba(0,0,0,.45);
  }
  .swoosh { position: absolute; left: 0; width: 100%; display: block; }
  .swoosh path.band { fill: var(--navy); }

  .brand {
    display: flex;
    align-items: center;
    gap: 7px;
    color: var(--sky);
    font-weight: 700;
    white-space: nowrap;
  }
  .brand-dot {
    flex: none;
    border-radius: 50%;
    background: var(--sky);
  }
  .contact { color: var(--ink); line-height: 1.55; white-space: nowrap; }
  .contact b { color: var(--sky); font-weight: 700; }

  /* Letterhead */
  .letterhead { left: 40px; top: 40px; width: 400px; height: 566px; background: var(--paper); }
  .letterhead .swoosh { top: 14px; height: 40px; }
  .letterhead .brand { position: absolute; left: 120px; top: 22px; font-size: 13px; }
  .letterhead .brand-dot { width: 16px; height: 16px; }
  .letterhead .contact { position: absolute; left: 143px; top: 48px; font-size: 6.5px; }

  /* Business cards */
  .card { top: 40px; width: 340px; height: 196px; }
  .card-front { left: 460px; background: linear-gradient(160deg, var(--blue) 0%, var(--blue-deep) 100%); }
  .card-back { left: 820px; background: var(--paper); }
  .card .brand { position: absolute; left: 22px; top: 58px; font-size: 14px; }
  .card .brand-dot { width: 18px; height: 18px; }
  .card-front .brand { color: var(--paper-white); }
  .card-front .brand-dot { background: var(--sky); }
  .card-details { position: absolute; left: 56px; top: 88px; font-size: 7px; line-height: 1.6; white-space: nowrap; }
  .card-details .full-name { font-size: 10px; letter-spacing: .04em; }
  .card-front .card-details { color: var(--paper-white); }
  .card-back .card-details { color: var(--ink); }
  .card-back .card-details .full-name { color: var(--blue); }
  .card-details .zh { font-family: "Noto Sans TC", sans-serif; }
  .card-art {
    position: absolute; right: 0; top: 0; width: 130px; height: 68px;
    background: radial-gradient(circle at 60% 50%, #ffffff 0%, #cfe3f3 40%, #3a7fc4 100%);
    opacity: .9;
  }
  .card .swoosh { bottom: 18px; height: 14px; }
  .card-front .swoosh path.band { fill: var(--rule-grey); }
  .card-back .swoosh.top { top: 0; bottom: auto; height: 12px; }
  .card-web { position: absolute; bottom: 5px; left: 0; width: 100%; text-align: center; font-size: 6.5px; }
  .card-front .card-web { color: var(--paper-white); }
  .card-back .card-web { color: var(--ink); }

  /* Envelope */
  .envelope { left: 500px; top: 270px; width: 660px; height: 340px; background: var(--paper); }
  .envelope-flap { position: absolute; top: 0; left: 0; width: 100%; height: 56px; display: block; }
  .envelope-flap path { fill: var(--blue); }
  .envelope .swoosh { top: 78px; height: 30px; }
  .envelope .brand { position: absolute; left: 292px; top: 86px; font-size: 17px; }
  .envelope .brand-dot { width: 24px; height: 24px; }
  .envelope .contact { position: absolute; left: 322px; top: 128px; font-size: 11px; line-height: 1.9; }
  .envelope-window {
    position: absolute; left: 332px; top: 244px; width: 300px; height: 66px;
    background: var(--paper-white); border-radius: 12px;
  }

  /* Presentation slides */
  .slide { top: 640px; width: 360px; height: 225px; }
  .slide-title { left: 420px; background: radial-gradient(ellipse at 50% 60%, #1f66c2 0%, var(--blue) 45%, var(--blue-deep) 100%); }
  .slide-content { background: var(--paper-white); }
  .slide-content.first { left: 40px; }
  .slide-content.second { left: 800px; }
  .slide-title .swoosh { top: 6px; height: 18px; }
  .slide-title .swoosh path.band { fill: var(--rule-grey); }
  .slide-title .brand { position: absolute; left: 0; right: 0; top: 24px; justify-content: center; font-size: 9px; color: var(--paper-white); }
  .slide-title .brand-dot { width: 11px; height: 11px; }
  .slide-content .swoosh { bottom: 8px; height: 22px; }
  .slide-content .brand { position: absolute; left: 0; right: 0; bottom: 14px; justify-content: center; font-size: 8px; }
  .slide-content .brand-dot { width: 10px; height: 10px; }
</style>
</head>
<body>
<main class="canvas">

  <!-- Letterhead -->
  <section class="piece letterhead" aria-label="Letterhead">
    <svg class="swoosh" viewBox="0 0 400 40" preserveAspectRatio="none" aria-hidden="true">
      <path class="band" d="M0 6 Q60 14 110 22 L110 26 Q50 20 0 12Z"/>
      <path class="band" d="M314 22 Q360 14 400 0 L400 7 Q360 22 314 27Z"/>
    </svg>
    <div class="brand"><span class="brand-dot"></span>Brisk Pebble Software</div>
    <div class="contact">
      <b>P</b>+886-2-25118340 | <b>F</b>+886-2-25118472<br>
      2F-7, NO. 26, Lane 91, Fulin Road, Nei Hu District, Taipei Taiwan
    </div>
  </section>

  <!-- Business card, front -->
  <section class="piece card card-front" aria-label="Business card front">
    <div class="card-art" role="img" aria-label="Playful mascot illustration corner"></div>
    <div class="brand"><span class="brand-dot"></span>Brisk Pebble Software</div>
    <div class="card-details">
      <div class="full-name">Full Name</div>
      <div>Occupation | name@briskpebble-example.com</div>
      <div>P+886-2-25118340 | M+886-2-25118340 | F+886-2-25118472</div>
      <div class="zh">台灣台北市內湖區富林路91巷26號2樓之7</div>
    </div>
    <svg class="swoosh" viewBox="0 0 340 14" preserveAspectRatio="none" aria-hidden="true">
      <path class="band" d="M0 0 Q170 10 340 0 L340 3 Q170 14 0 3Z"/>
    </svg>
    <div class="card-web">www.briskpebble-example.com</div>
  </section>

  <!-- Business card, back -->
  <section class="piece card card-back" aria-label="Business card back">
    <svg class="swoosh top" viewBox="0 0 340 12" preserveAspectRatio="none" aria-hidden="true">
      <path class="band" d="M0 0 Q170 12 340 0 L340 2 Q170 15 0 3Z"/>
    </svg>
    <div class="brand"><span class="brand-dot"></span>Brisk Pebble Software</div>
    <div class="card-details">
      <div class="full-name">Full Name</div>
      <div>Occupation | name@briskpebble-example.com</div>
      <div>P+886-2-25118340 | M+886-2-25118340 | F+886-2-25118472</div>
      <div>2F-7, NO. 26, Lane 91, Fulin Road, Nei Hu District, Taipei Taiwan</div>
    </div>
    <svg class="swoosh" viewBox="0 0 340 14" preserveAspectRatio="none" aria-hidden="true">
      <path class="band" d="M0 0 Q170 12 340 0 L340 3 Q170 16 0 4Z"/>
    </svg>
    <div class="card-web">www.briskpebble-example.com</div>
  </section>

  <!-- Envelope -->
  <section class="piece envelope" aria-label="Envelope">
    <svg class="envelope-flap" viewBox="0 0 660 56" preserveAspectRatio="none" aria-hidden="true">
      <path d="M0 0 H660 V44 Q330 56 0 44Z"/>
    </svg>
    <svg class="swoosh" viewBox="0 0 660 30" preserveAspectRatio="none" aria-hidden="true">
      <path class="band" d="M0 0 Q150 14 278 22 L278 26 Q130 20 0 6Z"/>
      <path class="band" d="M548 22 Q610 16 660 4 L660 10 Q610 22 548 27Z"/>
    </svg>
    <div class="brand"><span class="brand-dot"></span>Brisk Pebble Software</div>
    <div class="contact">
      <b>P</b>+886-2-25118340 | <b>F</b>+886-2-25118472<br>
      2F-7, NO. 26, Lane 91, Fulin Road, Nei Hu District, Taipei Taiwan
    </div>
    <div class="envelope-window"></div>
  </section>

  <!-- Presentation: content slide -->
  <section class="piece slide slide-content first" aria-label="Presentation content slide">
    <svg class="swoosh" viewBox="0 0 360 22" preserveAspectRatio="none" aria-hidden="true">
      <path class="band" d="M0 4 Q60 12 110 16 L110 19 Q55 16 0 9Z"/>
      <path class="band" d="M250 16 Q305 12 360 4 L360 9 Q305 16 250 19Z"/>
    </svg>
    <div class="brand"><span class="brand-dot"></span>Brisk Pebble Software</div>
  </section>

  <!-- Presentation: title slide -->
  <section class="piece slide slide-title" aria-label="Presentation title slide">
    <svg class="swoosh" viewBox="0 0 360 18" preserveAspectRatio="none" aria-hidden="true">
      <path class="band" d="M0 0 Q180 16 360 0 L360 3 Q180 20 0 3Z"/>
    </svg>
    <div class="brand"><span class="brand-dot"></span>Brisk Pebble Software</div>
  </section>

  <!-- Presentation: content slide -->
  <section class="piece slide slide-content second" aria-label="Presentation content slide">
    <svg class="swoosh" viewBox="0 0 360 22" preserveAspectRatio="none" aria-hidden="true">
      <path class="band" d="M0 4 Q60 12 110 16 L110 19 Q55 16 0 9Z"/>
      <path class="band" d="M250 16 Q305 12 360 4 L360 9 Q305 16 250 19Z"/>
    </svg>
    <div class="brand"><span class="brand-dot"></span>Brisk Pebble Software</div>
  </section>

</main>
</body>
</html>
```